Consumer Product Goods (Food) website

We need a simple, but clean and modern website for our new food branded company called Brightfern Foods.

Need a website that company can easily update. I added company logo and some images of our products. I added 1 package design of our products that's available now in the retail stores.

Company currently has 1 item but will be adding up to 5 items witin a few months. So need a website we can easily add new products.
Updates

Project Deadline Extended
Reason: We're guaranteeing payment and wanted to give more time for others to submit.

Target Market(s)

Customers that are seeking new adventurous novelty Asian foods.

Industry/Entity Type

Retail

Coding

Coded - Design and coding required

Number of Pages Required

3 page

Requirements
Must have
• I would like to have 3 pages: Homepage, Products Page, and Contact Us.
Nice to have
• I would like a nice visually clean and modern looking homepage. As you can see from the package design, it has a dark tone, so if we can try to make the website a dark blackgroup. I uploaded the dark background we used in our package. Maybe have the 3 different dumplings rotating images on the homepage.
• Products Page should have just 1 product right now; Kimchi & Pork dumplings. Maybe have like pic of the package design and have space for a briefly summary of product, ingredient list and nutrition fact. Should be a page where i can add more products to this page.
• Contact Us page can simply have map, email addres, and phone #.
• would be nice to have where the website is responsive to PC, tablet, and mobile phones

```html
<!DOCTYPE html>
<html lang="en">
<head>
<meta charset="utf-8">
<title>Brightfern Foods — Kimchi &amp; Pork Dumplings</title>
<link rel="stylesheet" href="https://fonts.googleapis.com/css2?family=Montserrat:wght@400;500;600;700&family=Noto+Serif:wght@400&display=swap">
<style>
  :root {
    --ink: #ffffff;
    --muted: #8a8a8a;
    --wood-dark: #0d0d0d;
    --wood-mid: #1f1f1f;
    --wood-light: #2c2a28;
    --leaf: #7dc242;
    --rule: rgba(255,255,255,0.08);
  }
  * { margin: 0; padding: 0; box-sizing: border-box; }
  html, body { width: 1200px; height: 900px; overflow: hidden; background: var(--wood-dark); }
  body { font-family: "Montserrat", sans-serif; color: var(--ink); }

  .page { position: relative; width: 1200px; height: 900px; overflow: hidden; }

  .wood-backdrop {
    position: absolute; inset: 0;
    background:
      radial-gradient(ellipse 520px 420px at 600px 440px, rgba(60,56,52,0.55), transparent 70%),
      linear-gradient(180deg, var(--wood-mid) 0%, #161514 40%, var(--wood-light) 75%, #141312 100%);
  }

  .dish-photo {
    position: absolute; left: 344px; top: 352px; width: 508px; height: 292px;
    border-radius: 50%;
    background: radial-gradient(ellipse at 50% 40%, #c9b98d 0%, #a89a6f 30%, #3b3a36 62%, #111 80%);
    opacity: 0.85;
  }

  .main-nav { position: absolute; top: 57px; left: 160px; display: flex; }
  .main-nav a {
    color: var(--ink); text-decoration: none; font-size: 12.5px; font-weight: 500;
    letter-spacing: 0.2px; margin-right: 33px;
  }

  .brand {
    position: absolute; top: 60px; left: 0; width: 1200px;
    display: flex; flex-direction: column; align-items: center;
  }
  .brand-mark { width: 66px; height: 66px; background: var(--ink); border-radius: 14px; }
  .brand-name {
    margin-top: 14px; font-size: 19px; font-weight: 700; letter-spacing: 1px;
    color: var(--ink); text-transform: uppercase;
  }

  .contact-bar {
    position: absolute; top: 57px; left: 790px; display: flex; align-items: center;
    font-size: 10.5px; font-weight: 600;
  }
  .contact-item { display: flex; align-items: center; margin-right: 24px; }
  .contact-item svg { margin-right: 8px; }

  .hero-copy { position: absolute; top: 248px; left: 0; width: 1200px; text-align: center; }
  .hero-title {
    font-family: "Noto Serif", serif; font-weight: 400; font-size: 48px; line-height: 54px;
    letter-spacing: 0.5px; text-transform: uppercase;
  }
  .hero-divider { position: absolute; left: 311px; top: 372px; }
  .hero-text {
    position: absolute; top: 404px; left: 330px; width: 540px; text-align: center;
    font-size: 12px; font-weight: 500; line-height: 21px;
  }

  .read-more {
    position: absolute; left: 547px; top: 577px; width: 106px; height: 37px;
    background: var(--leaf); color: var(--ink); font-size: 11.5px; font-weight: 500;
    display: flex; align-items: center; justify-content: center; text-decoration: none;
  }

  .slider-arrow {
    position: absolute; top: 431px; width: 38px; height: 38px;
    border: 1px solid var(--ink); display: flex; align-items: center; justify-content: center;
  }
  .slider-arrow.prev { left: 75px; }
  .slider-arrow.next { left: 1087px; }

  .slider-dots { position: absolute; top: 808px; left: 572px; display: flex; }
  .slider-dots span {
    width: 11px; height: 11px; border-radius: 50%; border: 1.5px solid var(--ink); margin-right: 11px;
  }
  .slider-dots span.active { background: var(--ink); }

  .site-footer {
    position: absolute; top: 862px; left: 0; width: 1200px; height: 38px;
    border-top: 1px solid var(--rule); text-align: center;
    font-size: 10.5px; color: var(--muted); line-height: 38px;
  }
</style>
</head>
<body>
<div class="page">
  <div class="wood-backdrop" role="img" aria-label="Dark wooden tabletop background"></div>
  <div class="dish-photo" role="img" aria-label="Plate of kimchi and pork dumplings with lettuce and red onion"></div>

  <nav class="main-nav">
    <a href="#">HOME</a>
    <a href="#">PRODUCT</a>
    <a href="#">ABOUT</a>
    <a href="#">CONTACT</a>
  </nav>

  <div class="brand">
    <div class="brand-mark"></div>
    <div class="brand-name">Brightfern Foods</div>
  </div>

  <div class="contact-bar">
    <div class="contact-item">
      <svg width="13" height="13" viewBox="0 0 24 24"><path fill="#fff" d="M6.6 10.8a15.1 15.1 0 0 0 6.6 6.6l2.2-2.2a1 1 0 0 1 1-.25 11.4 11.4 0 0 0 3.6.57 1 1 0 0 1 1 1V20a1 1 0 0 1-1 1A17 17 0 0 1 3 4a1 1 0 0 1 1-1h3.5a1 1 0 0 1 1 1c0 1.25.2 2.45.57 3.57a1 1 0 0 1-.25 1z"/></svg>
      555 014 2290
    </div>
    <div class="contact-item">
      <svg width="16" height="12" viewBox="0 0 16 12"><rect width="16" height="12" rx="1.5" fill="#fff"/><path d="M1 1.5 8 7l7-5.5" fill="none" stroke="#1a1a1a" stroke-width="1.6"/></svg>
      hello@brightfernfoods.com
    </div>
  </div>

  <div class="hero-copy">
    <h1 class="hero-title">Kimchi &amp; Pork<br>Dumplings</h1>
  </div>

  <svg class="hero-divider" width="578" height="12" viewBox="0 0 578 12">
    <line x1="0" y1="6" x2="578" y2="6" stroke="#fff" stroke-width="1.5"/>
    <rect x="284" y="1" width="8" height="8" fill="#fff" transform="rotate(45 289 6)"/>
  </svg>

  <p class="hero-text">Inspired by the name of a famous trade route that connected East Asia and Western countries, Brightfern Foods was created to bring traditional .</p>

  <a class="read-more" href="#">READ MORE</a>

  <div class="slider-arrow prev">
    <svg width="10" height="14" viewBox="0 0 10 14"><path d="M8 1 2 7l6 6" fill="none" stroke="#fff" stroke-width="2"/></svg>
  </div>
  <div class="slider-arrow next">
    <svg width="10" height="14" viewBox="0 0 10 14"><path d="M2 1l6 6-6 6" fill="none" stroke="#fff" stroke-width="2"/></svg>
  </div>

  <div class="slider-dots">
    <span class="active"></span><span></span><span></span>
  </div>

  <footer class="site-footer">Brightfern Foods. © All Reserved 2016</footer>
</div>
</body>
</html>
```